International Used Food Processing Equipment company needs an awesome website!

We have been in business now for more than 15 years, and we are now launching a new website where international and USA based customers can view photos, descriptions, and ask questions of industrial food processing equipment.

We want the site to be vibrant and but yet communicate a professional tone to our customers. Most of our customers are older males, and the site must be easy to navigate, with easy on the eye color scheme. We want to features a lot of photos and a excellent equipment descriptions, with links where visitors can click on an item to send us a request for more information. We require easy to read font, clear navigation buttons and clear contact information to be found on each page.

Some of our competitors sites:
www.KVPTrade.com
www.lantorvalleyworks.com
www.pelvoxgroup.com

Our business name and logo is attached, but this is a rending of an image that was made about 10 years ago. Please let us know if you have any questions.

Target Market(s)

Food processing companies (canneries, fresh cut sector, large catering companies) in the USA and South America.

Logo Text

Excellent Machines at Excellent Prices

Coding

Coded - Design and coding required

Number of Pages Required

5+ page

Colors

Designer to choose colors to be used in the design.

Requirements
Must have
• Easy to navigate photo galleries, easy category search and easy machine search by keywords.
• Event Calendar
• Sign-up page for email newsletter
Nice to have
• Blog feature or latest news
• Past projects page
Should not have
• Hard to read font

```html
<!DOCTYPE html>
<html lang="en">
<head>
<meta charset="utf-8">
<title>The Kitchen Steward – Used Food Equipment</title>
<link href="https://fonts.googleapis.com/css2?family=Roboto:wght@400;500;700;900&family=Lato:wght@400;700&display=swap" rel="stylesheet">
<style>
:root{
  --red:#c4161c;
  --red-dark:#8e0f13;
  --ink:#1a1a1a;
  --text:#555;
  --muted:#8a8a8a;
  --light:#f2f2f2;
  --steel:#6f7378;
  --dark:#2b2b2b;
  --black:#141414;
  --white:#fff;
}
*{margin:0;padding:0;box-sizing:border-box}
html,body{width:1200px;height:3965px;overflow:hidden;background:var(--white)}
body{font-family:'Lato',sans-serif;color:var(--text);position:relative}
.abs{position:absolute}
h1,h2,h3,h4{font-family:'Roboto',sans-serif;color:var(--ink)}

/* header */
.site-header{top:0;left:0;width:1200px;height:117px;background:var(--white);z-index:3}
.brand{left:170px;top:14px;display:flex;align-items:center;gap:12px}
.brand-mark{width:34px;height:34px;background:var(--ink);border-radius:50%}
.brand-name{font-family:'Roboto',sans-serif;font-weight:700;font-size:20px;color:var(--ink);line-height:1.1}
.brand-tag{font-family:'Roboto',sans-serif;font-size:11px;color:var(--muted);margin-top:2px;font-weight:700}
.brand-point{left:180px;top:117px;width:0;height:0;border-left:22px solid transparent;border-right:22px solid transparent;border-top:50px solid var(--white);z-index:3}
.call{right:160px;top:30px;font-family:'Roboto',sans-serif;font-weight:700;font-size:17px;color:var(--red);display:flex;align-items:center;gap:8px}
.call b{color:var(--ink);font-weight:700}
.main-nav{right:160px;top:70px;display:flex;gap:26px;font-family:'Roboto',sans-serif;font-weight:500;font-size:16px;color:var(--ink)}

/* hero */
.hero{top:117px;left:0;width:1200px;height:590px;background:linear-gradient(180deg,#3a3d40 0%,#5b5e62 45%,#4a3030 85%,#2e2b2b 100%);clip-path:polygon(0 0,100% 0,100% 510px,600px 590px,0 510px)}
.hero-edge{top:117px;left:0;width:1200px;height:600px}
.hero-title{top:280px;left:0;width:1200px;text-align:center;color:var(--white);font-weight:900;font-size:44px;letter-spacing:.5px;line-height:1.1}
.hero-sub{top:333px;left:0;width:1200px;text-align:center;color:var(--white);font-family:'Roboto',sans-serif;font-weight:700;font-size:20px;line-height:1.2}
.search{top:380px;left:220px;display:flex;gap:6px}
.search .field{width:390px;height:50px;background:var(--white);display:flex;align-items:center;padding-left:16px;gap:10px;color:var(--muted);font-size:16px}
.search .select{width:195px;height:50px;background:var(--white);display:flex;align-items:center;justify-content:space-between;padding:0 16px;color:var(--muted);font-size:16px}
.search .btn{margin-left:8px;width:145px;height:50px;background:var(--red);color:var(--white);font-family:'Roboto',sans-serif;font-weight:700;font-size:17px;display:flex;align-items:center;justify-content:center}

/* section titles */
.rule{height:9px;background:repeating-linear-gradient(120deg,#777 0 2px,transparent 2px 5px)}
.section-title{width:1200px;left:0;text-align:center;font-weight:700;font-size:30px}

/* about */
.about-title{left:158px;top:772px;font-weight:700;font-size:30px}
.about-rule{left:160px;top:820px;width:165px}
.about-copy{left:158px;top:852px;width:450px;font-size:16px;line-height:1.5}
.about-copy p+p{margin-top:22px}
.btn-outline{left:160px;top:1043px;width:166px;height:46px;border:2px solid var(--red);color:var(--red);font-family:'Roboto',sans-serif;font-weight:500;font-size:14px;display:flex;align-items:center;justify-content:center}
.about-frame{left:670px;top:760px;width:370px;height:335px;border:3px solid #ccc}
.about-photo{left:688px;top:775px;width:335px;height:300px;background:linear-gradient(135deg,#e9ecef,#9aa0a6 55%,#5e6267)}
.corner-tr{left:985px;top:752px;width:56px;height:56px;border-top:12px solid var(--red);border-right:12px solid var(--red)}
.corner-bl{left:665px;top:1045px;width:56px;height:56px;border-bottom:12px solid var(--red);border-left:12px solid var(--red)}

/* services */
.services{top:1190px;left:0;width:1200px;height:380px;background:linear-gradient(90deg,#262626 0%,#3e3a3a 50%,#8b1418 80%,#b3161b 100%);clip-path:polygon(0 60px,600px 0,1200px 60px,1200px 320px,600px 380px,0 320px)}
.service-card{top:1302px;width:282px;height:212px;border:3px solid var(--white)}
.service-card .photo{position:absolute;inset:0;background:linear-gradient(160deg,#8c8f93,#3f4348)}
.service-card h3{position:absolute;top:72px;width:100%;text-align:center;color:var(--white);font-weight:700;font-size:21px}
.service-card .rule{position:absolute;top:103px;left:90px;width:96px;background:repeating-linear-gradient(120deg,#fff 0 2px,transparent 2px 5px)}
.service-card .tab{position:absolute;bottom:-14px;left:88px;width:106px;height:30px;background:var(--white);clip-path:polygon(10% 0,90% 0,100% 50%,90% 100%,10% 100%,0 50%);font-family:'Roboto',sans-serif;font-weight:700;font-size:14px;color:var(--ink);display:flex;align-items:center;justify-content:center}

/* events */
.events-band{top:1810px;left:0;width:1200px;height:400px;background:linear-gradient(180deg,#fff 0%,#d9d9d9 100%)}
.calendar{left:190px;top:1808px;width:360px;height:322px;background:var(--white);border:2px solid #ddd;border-radius:10px;box-shadow:0 2px 6px rgba(0,0,0,.08)}
.cal-head{position:absolute;left:34px;top:10px;width:290px;height:40px;border-radius:20px;background:var(--dark);color:var(--white);font-family:'Roboto',sans-serif;font-weight:700;font-size:20px;display:flex;align-items:center;justify-content:center}
.cal-arrow{position:absolute;top:8px;width:24px;height:24px;border:1px solid #999;border-radius:50%;display:flex;align-items:center;justify-content:center}
.cal-grid{position:absolute;left:20px;top:76px;width:320px;display:grid;grid-template-columns:repeat(7,1fr);row-gap:14px;text-align:center;font-family:'Roboto',sans-serif;font-size:17px;color:#444}
.cal-grid .dow{font-weight:700;color:var(--ink)}
.cal-grid .today span{display:inline-block;width:30px;height:30px;line-height:30px;border-radius:50%;background:var(--black);color:var(--white);margin-top:-4px}
.event{left:585px;width:460px;display:flex;gap:22px}
.event .photo{width:138px;height:138px;border-radius:50%;flex:none;background:radial-gradient(circle at 50% 40%,#9b7a5c,#3b2e26)}
.event h4{font-weight:400;font-size:24px;margin-top:10px}
.event p{font-size:13px;line-height:1.5;color:var(--muted);margin-top:4px;width:290px}
.event .more{font-family:'Roboto',sans-serif;font-weight:700;font-size:13px;color:var(--ink);margin-top:6px}

/* projects */
.projects{top:2210px;left:0;width:1200px;height:430px;background:linear-gradient(180deg,#4a4a4a 0%,#7a7a7a 60%,#9a9a9a 100%);clip-path:polygon(0 0,100% 0,100% 370px,600px 430px,0 370px)}
.projects-title{top:2258px;color:var(--white)}
.projects-rule{left:508px;top:2302px;width:184px;background:repeating-linear-gradient(120deg,#fff 0 2px,transparent 2px 5px)}
.project{top:2352px;width:205px;height:240px;background:var(--dark)}
.project .photo{height:135px;background:linear-gradient(160deg,#b58a56,#5a4836)}
.project h4{color:var(--white);font-size:14px;font-weight:700;text-align:center;margin-top:14px}
.project p{color:#ccc;font-size:10px;line-height:1.4;text-align:center;padding:4px 16px 0}
.project .more{color:#ccc;font-size:10px;text-align:center;font-weight:700;margin-top:2px}
.nav-arrow{top:2445px}

/* news */
.news-title{top:2730px}
.news-rule{left:512px;top:2775px;width:176px}
.news-card{top:2818px;width:276px;height:342px;background:var(--white);box-shadow:0 3px 10px rgba(0,0,0,.15)}
.news-card .photo{height:180px;background:linear-gradient(160deg,#aeb4ba,#4d5359)}
.news-card .date{position:absolute;top:132px;right:46px;width:100px;height:32px;background:var(--white);font-family:'Roboto',sans-serif;font-weight:700;font-size:12px;color:var(--ink);display:flex;align-items:center;justify-content:center;border-radius:3px 3px 0 0}
.news-card h4{font-size:16px;font-weight:700;line-height:1.2;padding:14px 36px 0}
.news-card p{font-size:11px;line-height:1.45;color:var(--muted);padding:8px 36px 0}
.news-card .btn{margin:14px 0 0 36px;width:110px;height:28px;background:var(--red);color:var(--white);font-family:'Roboto',sans-serif;font-weight:700;font-size:11px;display:flex;align-items:center;justify-content:center}

/* newsletter */
.newsletter{top:3225px;left:0;width:1200px;height:340px;background:linear-gradient(90deg,#2b2b2b 0%,#4b3030 55%,#b3161b 100%);clip-path:polygon(0 70px,600px 0,1200px 70px,1200px 340px,0 340px)}
.newsletter-title{top:3312px;left:0;width:1200px;text-align:center;color:var(--white);font-weight:900;font-size:32px;line-height:1.2;letter-spacing:.5px}
.newsletter-copy{top:3360px;left:0;width:1200px;text-align:center;color:var(--white);font-size:16px;line-height:1.4}
.subscribe{left:283px;top:3434px;width:637px;height:54px;background:var(--white);display:flex;align-items:center;justify-content:space-between;padding:0 8px 0 22px;font-family:'Roboto',sans-serif;font-size:14px;color:#444}
.subscribe .btn{width:150px;height:38px;background:var(--black);color:var(--white);font-weight:700;font-size:16px;display:flex;align-items:center;justify-content:center}

/* footer */
.site-footer{top:3555px;left:0;width:1200px;height:410px;background:var(--black);color:#c8c8c8;font-size:14px}
.foot-col{top:100px}
.foot-col h4{color:var(--white);font-size:17px;font-weight:700;margin-bottom:16px}
.foot-col li{list-style:none;line-height:26px}
.contact-line{display:flex;gap:12px;align-items:flex-start;margin-bottom:16px;line-height:1.35}
.social li{display:flex;align-items:center;gap:12px;line-height:34px}
.social .dot{width:24px;height:24px;border-radius:50%;background:var(--white)}
.foot-line{top:340px;left:0;width:1200px;height:1px;background:#333}
.copyright{top:370px;left:0;width:1200px;text-align:center;font-size:13px;color:#888}
</style>
</head>
<body>

<header class="site-header abs">
  <div class="brand abs">
    <span class="brand-mark"></span>
    <div>
      <div class="brand-name">The Kitchen Steward</div>
      <div class="brand-tag">Used Food Equipment</div>
    </div>
  </div>
  <div class="call abs">
    <svg width="18" height="18" viewBox="0 0 24 24"><path fill="#c4161c" d="M6.6 10.8a15.1 15.1 0 0 0 6.6 6.6l2.2-2.2a1 1 0 0 1 1-.25 11.4 11.4 0 0 0 3.6.57 1 1 0 0 1 1 1V20a1 1 0 0 1-1 1A17 17 0 0 1 3 4a1 1 0 0 1 1-1h3.5a1 1 0 0 1 1 1c0 1.25.2 2.45.57 3.57a1 1 0 0 1-.25 1z"/></svg>
    Call Us: <b>555 0142 7780</b>
  </div>
  <nav class="main-nav abs">
    <span>About Us</span><span>Used Equipment</span><span>Gallery</span><span>Projects</span><span>News</span><span>Contact Us</span>
  </nav>
</header>
<div class="brand-point abs"></div>

<section class="hero abs" role="img" aria-label="Photo of a stainless steel food processing plant"></section>
<svg class="hero-edge abs" width="1200" height="600" viewBox="0 0 1200 600"><polyline points="0,512 600,592 1200,512" fill="none" stroke="#9a9a9a" stroke-width="6"/></svg>
<h1 class="hero-title abs">FIND USED FOOD EQUIPMENT</h1>
<div class="hero-sub abs">PELLENTESQUE FAUCIBUS UT ACCUMSAN ULTRICIES</div>
<div class="search abs">
  <div class="field">
    <svg width="16" height="16" viewBox="0 0 24 24"><circle cx="10" cy="10" r="7" fill="none" stroke="#888" stroke-width="2.5"/><line x1="15" y1="15" x2="21" y2="21" stroke="#888" stroke-width="2.5"/></svg>
    Search Equipment
  </div>
  <div class="select">Category
    <svg width="12" height="8" viewBox="0 0 12 8"><polyline points="1,1 6,6 11,1" fill="none" stroke="#666" stroke-width="2"/></svg>
  </div>
  <div class="btn">SEARCH</div>
</div>

<h2 class="about-title abs">ABOUT OUR COMPANY</h2>
<div class="rule about-rule abs"></div>
<div class="about-copy abs">
  <p>Pellentesque faucibus Ut accumsan ultricies elit Maecenas at justo id velit placerat molestie Donec dictum lectus non odio Cras a ante vitae enim iaculis aliquam</p>
  <p>Mauris nunc quam venenatis nec euismod sit amet egestas placerat est Pellentesque habitant morbi tristique senectus et netus et malesuada fames ac turpis egestas Crada</p>
</div>
<div class="btn-outline abs">LEARN MORE</div>
<div class="about-frame abs"></div>
<div class="about-photo abs" role="img" aria-label="Photo of a stainless steel cooking kettle"></div>
<div class="corner-tr abs"></div>
<div class="corner-bl abs"></div>

<section class="services abs" role="img" aria-label="Background photo of a factory floor"></section>
<div class="service-card abs" style="left:160px">
  <div class="photo" role="img" aria-label="Photo of an equipment service workshop"></div>
  <h3>EQUIPMENTS SERVICE</h3><div class="rule"></div><div class="tab">VIEW ALL</div>
</div>
<div class="service-card abs" style="left:457px">
  <div class="photo" role="img" aria-label="Photo of used processing machines"></div>
  <h3>USED EQUIPMENTS</h3><div class="rule"></div><div class="tab">VIEW ALL</div>
</div>
<div class="service-card abs" style="left:755px">
  <div class="photo" role="img" aria-label="Photo of a packaging line"></div>
  <h3 style="top:60px;line-height:1.05">PACKAGING<br>EQUIPMENTS</h3><div class="rule"></div><div class="tab">VIEW ALL</div>
</div>

<h2 class="section-title abs" style="top:1702px">EVENT CALENDAR</h2>
<div class="rule abs" style="left:508px;top:1748px;width:184px"></div>
<div class="events-band abs"></div>
<div class="calendar abs">
  <div class="cal-head">
    <span class="cal-arrow" style="left:8px"><svg width="8" height="10" viewBox="0 0 8 10"><polyline points="6,1 2,5 6,9" fill="none" stroke="#fff" stroke-width="2"/></svg></span>
    FEB 2019
    <span class="cal-arrow" style="right:8px"><svg width="8" height="10" viewBox="0 0 8 10"><polyline points="2,1 6,5 2,9" fill="none" stroke="#fff" stroke-width="2"/></svg></span>
  </div>
  <div class="cal-grid">
    <span class="dow">MO</span><span class="dow">TU</span><span class="dow">WE</span><span class="dow">TH</span><span class="dow">FR</span><span class="dow">SA</span><span class="dow">SU</span>
    <span>1</span><span>2</span><span>3</span><span>4</span><span>5</span><span>6</span><span>7</span>
    <span>8</span><span>9</span><span>10</span><span>11</span><span>12</span><span class="today"><span>13</span></span><span>14</span>
    <span>15</span><span>16</span><span>17</span><span>18</span><span>19</span><span>20</span><span>21</span>
    <span>22</span><span>23</span><span>24</span><span>25</span><span>26</span><span>27</span><span>28</span>
  </div>
</div>
<div class="event abs" style="top:1822px">
  <div class="photo" role="img" aria-label="Photo of a trade show event"></div>
  <div><h4>Event Title here</h4><p>Donec convallis pede venenatis nibh Duis quam Nam eget lacus Aliquam erat volutpat Quisque dignissim congue</p><div class="more">CLICK HERE</div></div>
</div>
<div class="event abs" style="top:1992px">
  <div class="photo" role="img" aria-label="Photo of an evening industry gathering"></div>
  <div><h4>Event Title here</h4><p>Donec convallis pede venenatis nibh Duis quam Nam eget lacus Aliquam erat volutpat Quisque dignissim congue</p><div class="more">CLICK HERE</div></div>
</div>

<section class="projects abs"></section>
<h2 class="section-title projects-title abs">PAST PROJECTS</h2>
<div class="rule projects-rule abs"></div>
<svg class="nav-arrow abs" style="left:104px" width="22" height="34" viewBox="0 0 22 34"><polyline points="18,3 4,17 18,31" fill="none" stroke="#fff" stroke-width="4"/></svg>
<svg class="nav-arrow abs" style="left:1074px" width="22" height="34" viewBox="0 0 22 34"><polyline points="4,3 18,17 4,31" fill="none" stroke="#fff" stroke-width="4"/></svg>
<div class="project abs" style="left:152px"><div class="photo" role="img" aria-label="Photo of a completed processing line"></div><h4>PROJECT TITLE</h4><p>Donec convallis pede venenatis nibh Duis quam Nam eget lacus</p><div class="more">READ MORE</div></div>
<div class="project abs" style="left:383px"><div class="photo" role="img" aria-label="Photo of a baking production line"></div><h4>PROJECT TITLE</h4><p>Donec convallis pede venenatis nibh Duis quam Nam eget lacus</p><div class="more">READ MORE</div></div>
<div class="project abs" style="left:614px"><div class="photo" style="background:linear-gradient(160deg,#8f969c,#3c4247)" role="img" aria-label="Photo of an installation site"></div><h4>PROJECT TITLE</h4><p>Donec convallis pede venenatis nibh Duis quam Nam eget lacus</p><div class="more">READ MORE</div></div>
<div class="project abs" style="left:845px"><div class="photo" style="background:linear-gradient(160deg,#c9b8a4,#6e5a48)" role="img" aria-label="Photo of food packing work"></div><h4>PROJECT TITLE</h4><p>Donec convallis pede venenatis nibh Duis quam Nam eget lacus</p><div class="more">READ MORE</div></div>

<h2 class="section-title news-title abs">LATEST NEWS</h2>
<div class="rule news-rule abs"></div>
<article class="news-card abs" style="left:165px"><div class="photo" role="img" aria-label="Photo of a processing hall"></div><div class="date">JAN 20, 2019</div><h4>Duis non nunc Nulla rho ncus dictum metus</h4><p>Vivamus porttitor purus nisi eleifend libero a tempus libero lectus feugiat felis Morbi diam mauris viverra in gra</p><div class="btn">READ MORE</div></article>
<article class="news-card abs" style="left:464px"><div class="photo" style="background:linear-gradient(160deg,#7fa4c4,#33485a)" role="img" aria-label="Photo of bottling machinery"></div><div class="date">JAN 20, 2019</div><h4>Duis non nunc Nulla rho ncus dictum metus</h4><p>Vivamus porttitor purus nisi eleifend libero a tempus libero lectus feugiat felis Morbi diam mauris viverra in gra</p><div class="btn">READ MORE</div></article>
<article class="news-card abs" style="left:763px"><div class="photo" style="background:linear-gradient(160deg,#c3c6c9,#5a5f64)" role="img" aria-label="Photo of steel conveyor parts"></div><div class="date">JAN 20, 2019</div><h4>Duis non nunc Nulla rho ncus dictum metus</h4><p>Vivamus porttitor purus nisi eleifend libero a tempus libero lectus feugiat felis Morbi diam mauris viverra in gra</p><div class="btn">READ MORE</div></article>

<section class="newsletter abs" role="img" aria-label="Background photo of a factory interior"></section>
<h2 class="newsletter-title abs">SIGN UP OUR NEWSLETTERS</h2>
<div class="newsletter-copy abs">Lorem ipsum dolor sit amet consectetuer adipiscing elit Nam cursus Morbi ut mi<br>Nullam enim leo egestas id condimentum at</div>
<div class="subscribe abs"><span>EMAIL ADDRESS</span><span class="btn">SUBSCRIBE</span></div>

<footer class="site-footer abs">
  <div class="foot-col abs" style="left:165px;width:240px">
    <h4>CONTACT US</h4>
    <div class="contact-line"><svg width="14" height="18" viewBox="0 0 14 18"><path d="M7 1a6 6 0 0 0-6 6c0 4.5 6 10 6 10s6-5.5 6-10a6 6 0 0 0-6-6z" fill="none" stroke="#ccc" stroke-width="1.6"/><circle cx="7" cy="7" r="2" fill="#ccc"/></svg><span>48 Harlow Avenue #3B<br>Texas 75201 TX</span></div>
    <div class="contact-line"><svg width="16" height="16" viewBox="0 0 24 24"><path fill="#ccc" d="M6.6 10.8a15.1 15.1 0 0 0 6.6 6.6l2.2-2.2a1 1 0 0 1 1-.25 11.4 11.4 0 0 0 3.6.57 1 1 0 0 1 1 1V20a1 1 0 0 1-1 1A17 17 0 0 1 3 4a1 1 0 0 1 1-1h3.5a1 1 0 0 1 1 1c0 1.25.2 2.45.57 3.57a1 1 0 0 1-.25 1z"/></svg><span>555.310.4471</span></div>
    <div class="contact-line"><svg width="16" height="12" viewBox="0 0 16 12"><rect x="1" y="1" width="14" height="10" fill="none" stroke="#ccc" stroke-width="1.4"/><polyline points="1,1 8,7 15,1" fill="none" stroke="#ccc" stroke-width="1.4"/></svg><span>info@kitchensteward.com</span></div>
  </div>
  <div class="foot-col abs" style="left:455px"><h4>COMPANY</h4><ul><li>Home</li><li>About us</li><li>Services</li><li>Why Us</li><li>Contact</li></ul></div>
  <div class="foot-col abs" style="left:638px"><h4>RESOURCES</h4><ul><li>Resources</li><li>Projects</li><li>Gallery</li><li>News</li><li>Sitemap</li></ul></div>
  <div class="foot-col abs" style="left:862px"><h4>GET IN TOUCH</h4><ul class="social"><li><span class="dot"></span>Updates</li><li><span class="dot"></span>Community</li><li><span class="dot"></span>Network</li><li><span class="dot"></span>Photo Feed</li></ul></div>
  <div class="foot-line abs"></div>
  <div class="copyright abs">Copyright © 2019 All right reserved</div>
</footer>

</body>
</html>
```